Hvac and insulation company needs good looking business card design

We are hvac and insulation company and looking for a new business cards that look to today standards designs

Target Market(s)

homeowners

Industry/Entity Type

Hvac

Contact Information for Business Card

Name: Walter Brindley
Home comfort consultant
address: 4827 Moravia Ct #215 Oakland, CA 94602
office: 888-731-5096
cell: 510-842-3917
Lic.# 583164
Email: walter@corvane-hvac.example
Web: corvane-hvac.example

Requirements
Must have
• clean and sleek look
Nice to have
• simple with a clean look
Should not have
• to busy business card

```html
<!DOCTYPE html>
<html lang="en">
<head>
<meta charset="utf-8">
<title>Corvane Home Solutions – Business Card</title>
<link rel="stylesheet" href="https://fonts.googleapis.com/css2?family=Poppins:wght@400;500;600&display=swap">
<style>
  :root {
    --orange: #ee7f22;
    --orange-deep: #c9661c;
    --grey-swoosh: #707070;
    --grey-text: #5a5a5a;
    --logo-light: #dcdcdc;
    --white: #ffffff;
    --backdrop: #e4e4e4;
  }
  * { margin: 0; padding: 0; box-sizing: border-box; }
  html, body { width: 1200px; height: 900px; overflow: hidden; }
  body {
    background: var(--backdrop);
    font-family: "Poppins", sans-serif;
    position: relative;
  }
  .card {
    position: absolute;
    left: 285px;
    width: 630px;
    height: 360px;
    border-radius: 18px;
    overflow: hidden;
    box-shadow: 0 10px 28px rgba(0,0,0,0.22);
  }
  .card-front { top: 70px; background: linear-gradient(135deg, #f2f2f2, var(--white) 55%); }
  .card-back {
    top: 470px;
    background: linear-gradient(135deg, var(--orange-deep), var(--orange) 55%, #f08a30);
  }
  .front-waves { position: absolute; inset: 0; }

  .brand { position: absolute; display: flex; align-items: center; }
  .brand-mark { background: var(--orange); }
  .brand-name { font-weight: 600; color: var(--orange); line-height: 1; letter-spacing: -0.5px; }
  .brand-tagline { color: var(--grey-text); letter-spacing: 3px; font-weight: 400; }

  .card-front .brand { top: 40px; left: 60px; gap: 12px; }
  .card-front .brand-mark { width: 30px; height: 30px; }
  .card-front .brand-name { font-size: 46px; }
  .card-front .brand-tagline { font-size: 11px; margin-top: 2px; }

  .person { position: absolute; top: 126px; right: 48px; text-align: right; }
  .person-name { color: var(--orange); font-size: 24px; font-weight: 500; text-transform: uppercase; letter-spacing: 0.5px; line-height: 1.3; }
  .person-title { color: var(--grey-text); font-size: 14px; letter-spacing: 0.5px; }

  .contact {
    position: absolute; right: 34px; bottom: 16px;
    color: var(--white); font-size: 13px; line-height: 1.4; text-align: right;
    list-style: none;
  }
  .contact-address { margin-bottom: 6px; padding-right: 22px; }
  .contact li { display: flex; justify-content: flex-end; align-items: center; gap: 8px; }
  .contact-icon { width: 14px; height: 14px; flex: none; }

  .card-back .brand { top: 118px; left: 50%; transform: translateX(-50%); gap: 16px; }
  .card-back .brand-mark { width: 42px; height: 42px; background: var(--logo-light); }
  .card-back .brand-name { font-size: 74px; color: var(--logo-light); }
  .card-back .brand-tagline { font-size: 16px; color: var(--logo-light); letter-spacing: 5px; }
  .license { position: absolute; bottom: 46px; width: 100%; text-align: center; color: var(--logo-light); font-size: 18px; letter-spacing: 1px; }
</style>
</head>
<body>

<section class="card card-front" aria-label="Business card front">
  <svg class="front-waves" viewBox="0 0 630 360" width="630" height="360" aria-hidden="true">
    <path d="M0,112 C40,165 180,196 330,202 C200,194 70,176 0,138 Z" fill="var(--grey-swoosh)"/>
    <path d="M0,150 C150,212 330,200 450,200 C540,200 600,208 630,220 L630,360 L0,360 Z" fill="var(--orange)"/>
    <path d="M0,170 C150,228 300,214 400,214" fill="none" stroke="var(--white)" stroke-width="4"/>
  </svg>

  <div class="brand">
    <span class="brand-mark"></span>
    <div>
      <div class="brand-name">corvane</div>
      <div class="brand-tagline">home solutions</div>
    </div>
  </div>

  <div class="person">
    <h1 class="person-name">Walter Brindley</h1>
    <p class="person-title">Home comfort consultant</p>
  </div>

  <ul class="contact">
    <li class="contact-address">4827 Moravia Ct<br>#215 Oakland, CA 94602</li>
    <li>888-731-5096
      <svg class="contact-icon" viewBox="0 0 14 14" aria-hidden="true"><path d="M3 1.5l2 2.5-1.2 1.5c.8 1.8 2 3 3.7 3.7L9 8l2.5 2-1 2C6 12 2 8 2 2.5z" fill="none" stroke="currentColor" stroke-width="1.2"/></svg>
    </li>
    <li>510-842-3917
      <svg class="contact-icon" viewBox="0 0 14 14" aria-hidden="true"><rect x="4" y="1.5" width="6" height="11" rx="1" fill="none" stroke="currentColor" stroke-width="1.2"/><circle cx="7" cy="10.5" r="0.7" fill="currentColor"/></svg>
    </li>
    <li>walter@corvane-hvac.example
      <svg class="contact-icon" viewBox="0 0 14 14" aria-hidden="true"><rect x="1.5" y="3" width="11" height="8" fill="none" stroke="currentColor" stroke-width="1.2"/><path d="M1.5 3.5L7 8l5.5-4.5" fill="none" stroke="currentColor" stroke-width="1.2"/></svg>
    </li>
    <li>www.corvane-hvac.example
      <svg class="contact-icon" viewBox="0 0 14 14" aria-hidden="true"><circle cx="7" cy="7" r="5.5" fill="none" stroke="currentColor" stroke-width="1.2"/><ellipse cx="7" cy="7" rx="2.3" ry="5.5" fill="none" stroke="currentColor" stroke-width="1"/><path d="M1.5 7h11" stroke="currentColor" stroke-width="1"/></svg>
    </li>
  </ul>
</section>

<section class="card card-back" aria-label="Business card back">
  <div class="brand">
    <span class="brand-mark"></span>
    <div>
      <div class="brand-name">corvane</div>
      <div class="brand-tagline">home solutions</div>
    </div>
  </div>
  <p class="license">Lic.# 583164</p>
</section>

</body>
</html>
```